TALL WAVE

I am in this industry for last 15 years we have done lots of commercial site like we work with ORBEL costruction, loam properties, DRV, quill construction.
We do all domestic and commercial wall and floor tiling, swimming pools, spas, paving, marbles blue stones and muchmore.

Specializing in the wall and floor Tiling, Waterproofing and floor preparations

Industry/Entity Type

Industry

Number of Pages Required

1 page

Font styles to use
Serif
Decorative

Colors

Designer to choose colors to be used in the design.

Requirements
Must have
• domestic and commercial indoor tiling, bathroom tiling and paving pictures
Nice to have
• beautiful bathroom pictures with tile

```html
<!DOCTYPE html>
<html lang="en">
<head>
<meta charset="utf-8">
<title>Tall Wave — Tiling, Paving &amp; Floor Preparations</title>
<link rel="stylesheet" href="https://fonts.googleapis.com/css2?family=Playfair+Display:ital,wght@0,700;1,700&family=Montserrat:wght@500&family=Source+Sans+3:wght@400&display=swap">
<style>
:root{
  --page-bg:#f5f3f4;
  --white:#ffffff;
  --ink:#111111;
  --text:#2a2a2a;
  --header-bg:#000000;
  --footer-bg:#2f2f2f;
  --footer-text:#e8e8e8;
  --dot:#333333;
}
*{margin:0;padding:0;box-sizing:border-box}
html,body{width:1200px;height:1000px;overflow:hidden;background:var(--page-bg)}
body{position:relative;font-family:"Source Sans 3",Arial,sans-serif;color:var(--text)}
.site{position:absolute;left:276px;top:0;width:648px;height:1000px;background:var(--white)}
.abs{position:absolute}

/* header */
.site-header{position:absolute;left:0;top:0;width:648px;height:27px;background:var(--header-bg)}
.brand{position:absolute;left:61px;top:3px;font-family:"Playfair Display",Georgia,serif;font-weight:700;font-size:17px;color:var(--white);line-height:20px}
.main-nav{position:absolute;top:9px;left:0;font-family:"Montserrat",Arial,sans-serif;font-weight:500;font-size:7.3px;letter-spacing:.3px;color:var(--white);text-transform:uppercase}
.main-nav span{position:absolute;white-space:nowrap;line-height:10px}
.social{position:absolute;display:flex}
.social i{display:block;border-radius:50%;background:var(--white)}
.social.small{gap:7px}
.social.small i{width:7px;height:7px}
.social.foot{gap:9px}
.social.foot i{width:9px;height:9px}

/* hero */
.hero{position:absolute;left:0;top:27px;width:648px;height:222px;
  background:linear-gradient(90deg,#7d7f80 0%,#c9c8c4 10%,#b7b3ad 35%,#8a6a48 50%,#9a9894 70%,#6d6f70 92%,#4e5052 100%)}
.hero-shade{position:absolute;inset:0;background:linear-gradient(180deg,rgba(0,0,0,.05),rgba(0,0,0,.25))}
.hero-title{position:absolute;left:0;width:678px;top:113px;text-align:center;font-family:"Playfair Display",Georgia,serif;font-weight:700;font-size:22.5px;color:var(--white);line-height:26px}
.hero-text{position:absolute;left:204px;width:240px;top:148px;text-align:center;font-size:7.5px;line-height:12px;color:var(--white)}
.hero-dots{position:absolute;left:312px;top:196px;display:flex;gap:5px}
.hero-dots i{width:4px;height:4px;border-radius:50%;border:1px solid var(--white)}
.hero-dots i.on{background:var(--white)}

/* sections */
.section-title{position:absolute;left:0;width:648px;text-align:center;font-family:"Playfair Display",Georgia,serif;font-style:italic;font-weight:700;font-size:19px;color:var(--ink);line-height:24px}
.photo{position:absolute}
.card-title{position:absolute;font-family:"Playfair Display",Georgia,serif;font-weight:700;font-size:11.2px;letter-spacing:.5px;color:var(--ink);white-space:nowrap;line-height:14px}
.card-text{position:absolute;font-size:7.5px;line-height:9.5px;color:var(--text)}
.pager{position:absolute;display:flex;gap:2px}
.pager i{width:3px;height:3px;background:var(--dot);border-radius:50%}
.pager i.off{background:#bbb}

/* footer */
.site-footer{position:absolute;left:0;top:822px;width:648px;height:178px;background:var(--footer-bg);color:var(--footer-text)}
.footer-heading{position:absolute;top:26px;font-family:"Playfair Display",Georgia,serif;font-weight:700;font-size:12.5px;color:var(--white);line-height:16px}
.footer-text{position:absolute;font-size:7px;line-height:13.3px;color:var(--footer-text)}
.newsletter-note{font-size:6.6px;line-height:10.5px}
.email-field{position:absolute;left:329px;top:91px;width:90px;height:14px;border:1px solid #bdbdbd;font-size:6.5px;line-height:12px;padding-left:6px;color:var(--footer-text)}
.email-field svg{position:absolute;right:6px;top:3px}
.copyright{position:absolute;right:58px;top:128px;font-size:6.3px;color:var(--footer-text)}
</style>
</head>
<body>
<div class="site">

  <header class="site-header">
    <div class="brand">Tall Wave</div>
    <nav class="main-nav">
      <span style="left:241px">Home</span>
      <span style="left:286px">About us</span>
      <span style="left:347px">Products</span>
      <span style="left:410px">Contact us</span>
    </nav>
    <div class="social small" style="left:550px;top:10px"><i></i><i></i><i></i></div>
  </header>

  <section class="hero">
    <div role="img" aria-label="Bright bathroom with wooden vanity, mirror cabinet, grey wall tiles and a glass shower" style="position:absolute;inset:0"></div>
    <div class="hero-shade"></div>
    <svg class="abs" style="left:14px;top:85px" width="14" height="24" viewBox="0 0 14 24"><path d="M12 1 L2 12 L12 23" fill="none" stroke="#fff" stroke-width="1.6"/></svg>
    <svg class="abs" style="left:618px;top:85px" width="14" height="24" viewBox="0 0 14 24"><path d="M2 1 L12 12 L2 23" fill="none" stroke="#fff" stroke-width="1.6"/></svg>
    <h1 class="hero-title">Lorem ipsum dolor sit amet</h1>
    <p class="hero-text">Cum sociis natoque penatibus et magnis dis parturi-<br>ent montes, nascetur ridiculus mus.</p>
    <div class="hero-dots"><i class="on"></i><i></i><i></i></div>
  </section>

  <h2 class="section-title" style="top:271px">Tiling &amp; Paving</h2>
  <svg class="abs" style="left:28px;top:369px" width="12" height="24" viewBox="0 0 12 24"><path d="M11 1 L1 12 L11 23" fill="none" stroke="#999" stroke-width="1.2"/></svg>
  <svg class="abs" style="left:604px;top:369px" width="12" height="24" viewBox="0 0 12 24"><path d="M1 1 L11 12 L1 23" fill="none" stroke="#999" stroke-width="1.2"/></svg>

  <div class="photo" role="img" aria-label="Modern kitchen with dark wall tiles, white island and bar stools" style="left:61px;top:315px;width:167px;height:166px;background:linear-gradient(160deg,#5a5d60 0%,#d9d6d0 45%,#8a5a34 75%,#6b4a30 100%)"></div>
  <div class="photo" role="img" aria-label="Gloved hand setting a tile with notched adhesive" style="left:241px;top:315px;width:166px;height:166px;background:linear-gradient(135deg,#c9c5bd 0%,#a06a3a 40%,#b98654 65%,#e4e2de 100%)"></div>
  <div class="photo" role="img" aria-label="Grey tiled bathroom with bathtub and towel rail" style="left:421px;top:315px;width:165px;height:166px;background:linear-gradient(170deg,#8c9094 0%,#b5b8bb 45%,#8f7b68 80%,#6f6a66 100%)"></div>

  <h3 class="card-title" style="left:61px;top:487px">Domestic Tiling</h3>
  <p class="card-text" style="left:61px;top:505px;width:135px">Cum sociis natoque penatibus et magnis dis parturient montes, nascetur ridiculus mus.</p>
  <h3 class="card-title" style="left:241px;top:487px">Commercial Tiling &amp; Paving</h3>
  <p class="card-text" style="left:241px;top:505px;width:150px">Cum sociis natoque penatibus et magnis dis partu-rient montes, nascetur ridiculus mus.</p>
  <h3 class="card-title" style="left:421px;top:487px">Bathroom Tiling</h3>
  <p class="card-text" style="left:421px;top:505px;width:135px">Cum sociis natoque penatibus et magnis dis parturient montes, nascetur ridiculus mus.</p>
  <div class="pager" style="left:320px;top:536px"><i></i><i class="off"></i></div>

  <h2 class="section-title" style="top:560px">Water proofing &amp; Floor Preparations</h2>

  <div class="photo" role="img" aria-label="Building site with waterproofed concrete foundation and workers" style="left:61px;top:608px;width:256px;height:146px;background:linear-gradient(170deg,#b8a890 0%,#8c8a86 35%,#5e6468 60%,#9b8f7e 100%)"></div>
  <div class="photo" role="img" aria-label="Worker laying wooden floor boards over a green underlay" style="left:330px;top:607px;width:256px;height:147px;background:linear-gradient(120deg,#4fc9b4 0%,#68d6c2 30%,#7a746e 55%,#8a847e 100%)"></div>

  <h3 class="card-title" style="left:61px;top:761px">Waterproofing The Floor</h3>
  <p class="card-text" style="left:61px;top:778px;width:170px">&nbsp;Cum sociis natoque penatibus et magnis dis partu-rient montes, nascetur ridiculus mus.</p>
  <h3 class="card-title" style="left:330px;top:761px">Floor Preparations</h3>
  <p class="card-text" style="left:330px;top:778px;width:170px">Cum sociis natoque penatibus et magnis dis partu-rient montes, nascetur ridiculus mus.</p>

  <footer class="site-footer">
    <h4 class="footer-heading" style="left:60px">Tall Wave</h4>
    <p class="footer-text" style="left:61px;top:52px;width:88px;line-height:10.5px">We do all domestic and commercial wall and floor tiling, swimming pools, spas, paving.</p>

    <h4 class="footer-heading" style="left:195px">Pages</h4>
    <p class="footer-text" style="left:196px;top:51px">FAQs<br>Support<br>Community<br>Sitemap</p>
    <p class="footer-text" style="left:241px;top:51px">Home<br>About us<br>Services<br>Contact us</p>

    <h4 class="footer-heading" style="left:330px">Our Newsletter</h4>
    <p class="footer-text newsletter-note" style="left:330px;top:52px;width:112px">Subscribe to our newsletter and we will inform you about newer proj-ects and promotions</p>
    <div class="email-field">Email address...
      <svg width="8" height="6" viewBox="0 0 8 6"><path d="M0 3 H7 M5 1 L7 3 L5 5" fill="none" stroke="#ddd" stroke-width=".8"/></svg>
    </div>

    <h4 class="footer-heading" style="left:496px">Contact Us</h4>
    <p class="footer-text" style="left:497px;top:51px">Larkhill Row, 58120<br>Brindle Vale.<br>info@tallwave.co<br>Tel 0198 765 4321</p>

    <div class="social foot" style="left:63px;top:128px"><i></i><i></i><i></i></div>
    <p class="copyright">© Copyrights reserved Tall Wave Co.Ltd</p>
  </footer>
</div>
</body>
</html>
```